Start up Dialysis Clinic needs its first website - Torvane Health

Create a visually appealing and user-friendly website for Torvane Health, a dialysis clinic located in Mt. Irvine, Tobago. The website should effectively communicate our services to local, regional, and international patients, providing essential information and fostering trust and engagement..
Key Goals:

1. Informative: Provide comprehensive information about our services, facility, and team.
2. User-Friendly: Ensure the website is easy to navigate, with a clear structure and accessible content.
3. Engaging: Create a visually appealing design that reflects the professionalism and care of Torvane Health.
4. Responsive: Ensure the website is fully responsive and performs well on all devices, including desktops, tablets, and smartphones.
5. Trust-Building: Include testimonials, credentials, and patient resources to build trust with potential patients.
Scope of Work:

1. Home Page: An inviting and informative landing page that provides an overview of our clinic, mission, and services. Include a call to action for more information and contact details.
2. About Us: A detailed page about Torvane Health, including our mission, vision, team, and facility tour.
3. Services: A comprehensive page describing the dialysis services we offer, including Hemodialysis, Peritoneal Dialysis, and Home Hemodialysis.
4. Patient Information: A resourceful section with guides for new patients, FAQs, insurance and billing information, and downloadable forms.
5. Resources: Educational content about kidney health, dialysis options, diet and nutrition tips, and support groups.
6. Contact Us: A contact page with our address, phone number, email, office hours, a contact form, and a map.

```html
<!DOCTYPE html>
<html lang="en">
<head>
<meta charset="utf-8">
<title>Torvane Health</title>
<link href="https://fonts.googleapis.com/css2?family=Open+Sans:wght@600;700&family=Roboto:wght@400;500;700&display=swap" rel="stylesheet">
<style>
:root{
  --blue:#3c78c3;
  --green:#6aa740;
  --grad:linear-gradient(90deg,#4378bf 0%,#6aa740 100%);
  --grad-btn:linear-gradient(90deg,#6aa740 0%,#3f77c2 100%);
  --ink:#1d1d1d;
  --text:#6d6d6d;
  --soft:#f2f2f2;
  --white:#ffffff;
  --black:#050505;
}
*{margin:0;padding:0;box-sizing:border-box}
html,body{width:1200px;height:4766px;overflow:hidden}
body{position:relative;background:var(--white);font-family:"Roboto",Arial,sans-serif;color:var(--ink)}
.abs{position:absolute}
.heading{font-family:"Open Sans",Arial,sans-serif;font-weight:600;letter-spacing:.5px;text-transform:uppercase}
.btn{position:absolute;display:flex;align-items:center;justify-content:center;gap:7px;color:#fff;font-weight:700;font-size:13px;text-transform:uppercase;border-radius:3px;background:var(--grad-btn);box-shadow:0 3px 6px rgba(0,0,0,.18)}
.btn svg{width:12px;height:12px}
.photo{position:absolute}

/* header */
.topbar{left:472px;top:0;width:728px;height:52px;background:var(--blue);clip-path:polygon(22px 0,100% 0,100% 100%,0 100%)}
.contact-chip{position:absolute;top:8px;display:flex;align-items:center;gap:12px;color:#fff;font-size:12px;line-height:15px}
.contact-chip .ico{width:30px;height:30px;background:var(--green);border-radius:4px;display:flex;align-items:center;justify-content:center}
.contact-chip small{display:block;font-size:10px;opacity:.85}
.contact-chip strong{font-weight:500}
.book{left:927px;top:7px;width:130px;height:37px;background:var(--green);font-size:12px;border-radius:3px;box-shadow:none}
.nav{position:absolute;top:70px;left:425px;display:flex;gap:0;font-size:13.5px;font-weight:500;color:var(--ink)}
.nav a{position:absolute;white-space:nowrap;color:inherit;text-decoration:none}
.brand-box{left:166px;top:0;width:164px;height:150px;background:#fff;clip-path:polygon(0 0,100% 0,100% 82%,88% 100%,12% 100%,0 82%);z-index:3;display:flex;flex-direction:column;align-items:center;justify-content:center;gap:8px}
.brand-mark{width:34px;height:34px;background:var(--blue)}
.brand-name{font-family:"Open Sans",Arial,sans-serif;font-weight:700;font-size:19px;color:var(--blue);text-transform:uppercase;text-align:center;line-height:21px}

/* hero */
.hero{left:0;top:105px;width:1200px;height:630px;background:linear-gradient(100deg,#c9d8b6 0%,#94b079 30%,#6f9160 55%,#8fa67a 75%,#5e7a4c 100%)}
.hero-shade{left:0;top:105px;width:700px;height:630px;background:linear-gradient(90deg,rgba(40,60,30,.45),rgba(40,60,30,0))}
.hero-title{left:144px;top:300px;color:#fff;font-size:40px;font-weight:700;letter-spacing:1.5px}
.hero-text{left:144px;top:364px;width:420px;color:#fff;font-size:14.5px;line-height:25px;font-weight:500}
.arrow-dark{width:38px;height:38px;border-radius:50%;background:rgba(0,0,0,.55);display:flex;align-items:center;justify-content:center}

/* about */
.about-panel{left:144px;top:830px;width:445px;height:461px;background:linear-gradient(45deg,#3f77c2 0%,#5a9a6d 55%,#6aa740 100%);display:flex;align-items:center;justify-content:center}
.about-panel span{font-family:"Open Sans",Arial,sans-serif;font-weight:700;font-size:34px;color:#fff;text-transform:uppercase;letter-spacing:2px}
.section-title{font-size:35px;color:var(--ink)}
.body-copy{font-size:13px;line-height:25px;color:var(--text)}

/* services */
.services{left:0;top:1383px;width:1200px;height:682px;background:var(--soft)}
.card{position:absolute;width:287px;background:#fff;border-radius:6px;box-shadow:0 4px 14px rgba(0,0,0,.18);text-align:center}
.card .photo{left:7px;top:7px;width:273px;height:198px;border-radius:3px}
.card .icon{position:absolute;left:108px;top:168px;width:70px;height:70px;border-radius:50%;background:var(--blue);border:4px solid #fff;display:flex;align-items:center;justify-content:center}
.card h3{position:absolute;left:0;width:100%;top:250px;font-size:17px;font-weight:500}
.card p{position:absolute;left:18px;width:251px;top:280px;font-size:12.5px;line-height:21px;color:var(--text)}
.card .btn{left:69px;top:355px;width:148px;height:40px;font-size:12px}

/* holiday band */
.band{left:0;top:2065px;width:1200px;height:346px;background:var(--grad);text-align:center;color:#fff}
.band h2{position:absolute;left:0;width:100%;top:62px;font-size:30px;line-height:43px;font-weight:600}
.band p{position:absolute;left:240px;width:720px;top:160px;font-size:13px;line-height:23px}
.call-pill{position:absolute;left:477px;top:233px;width:246px;height:43px;background:#fff;border-radius:22px;display:flex;align-items:center;gap:12px;padding-left:4px;color:var(--blue);font-size:13px;font-weight:700;text-transform:uppercase}
.call-pill .ico{width:35px;height:35px;border-radius:50%;background:var(--green);display:flex;align-items:center;justify-content:center}

/* testimonials */
.t-title{left:0;width:1200px;top:3145px;text-align:center;color:#fff;font-size:31px}
.t-card{position:absolute;top:3236px;width:381px;height:214px;background:#fff;border-radius:22px;box-shadow:0 4px 12px rgba(0,0,0,.2)}
.t-card .quote{position:absolute;left:96px;top:18px;font-family:Georgia,serif;font-size:60px;line-height:60px;color:var(--green);font-weight:700}
.t-card p{position:absolute;left:96px;top:72px;width:255px;font-size:12.5px;line-height:22px;color:var(--text)}
.t-card h4{position:absolute;left:96px;top:150px;font-size:14.5px;font-weight:500}
.t-card .stars{position:absolute;left:96px;top:168px;color:#f4a512;font-size:15px;letter-spacing:1px}
.avatar{position:absolute;width:110px;height:110px;border-radius:50%;border:4px solid #fff;background:linear-gradient(160deg,#cfd6dc,#6f7f8c)}

/* blog */
.blog-cell{position:absolute;width:303px;height:269px;background:#fff}
.blog-cell .date{position:absolute;left:20px;top:38px;font-size:11.5px;color:var(--green);display:flex;align-items:center;gap:4px;font-weight:500}
.blog-cell h3{position:absolute;left:20px;top:60px;width:240px;font-size:15.5px;line-height:23px;font-weight:700}
.blog-cell p{position:absolute;left:20px;top:120px;width:250px;font-size:12px;line-height:21px;color:var(--text)}
.blog-cell .btn{left:20px;top:210px;width:136px;height:36px;font-size:12px;background:linear-gradient(90deg,#3f77c2,#4b8ab0)}
.blog-grid{left:146px;top:3750px;width:908px;height:538px;box-shadow:0 2px 14px rgba(0,0,0,.12)}

/* footer */
.foot-title{position:absolute;top:4488px;color:#fff;font-size:15px;font-weight:700}
.foot-item{position:absolute;left:409px;display:flex;gap:10px;color:#fff;font-size:11.5px;line-height:15px}
.foot-item b{display:block;font-size:10px}
.foot-links{position:absolute;left:690px;top:4527px;color:#fff;font-size:12px;line-height:24.5px;list-style:none}
.foot-note{position:absolute;left:843px;top:4530px;width:220px;color:#fff;font-size:11.5px;line-height:17px}
.foot-bottom{position:absolute;top:4726px;color:#fff;font-size:12px}
.social{width:13px;height:13px;border-radius:50%;background:#fff;position:absolute;top:4728px}
</style>
</head>
<body>

<!-- header -->
<div class="abs topbar">
  <div class="contact-chip" style="left:65px">
    <div class="ico"><svg width="16" height="16" viewBox="0 0 24 24" fill="none" stroke="#fff" stroke-width="2"><circle cx="12" cy="8" r="4"/><path d="M4 21c1-5 15-5 16 0"/></svg></div>
    <div><small>Email</small><strong>info@torvanehealth.com</strong></div>
  </div>
  <div class="contact-chip" style="left:270px">
    <div class="ico"><svg width="16" height="16" viewBox="0 0 24 24" fill="#fff"><path d="M6.6 10.8a15 15 0 0 0 6.6 6.6l2.2-2.2c.3-.3.7-.4 1-.2 1.1.4 2.3.6 3.6.6.6 0 1 .4 1 1V20c0 .6-.4 1-1 1A17 17 0 0 1 3 4c0-.6.4-1 1-1h3.5c.6 0 1 .4 1 1 0 1.3.2 2.5.6 3.6.1.3 0 .7-.2 1z"/></svg></div>
    <div><small>Call or text us</small><strong style="font-size:14px">(888) 888-8888</strong></div>
  </div>
</div>
<div class="btn book">Book Now</div>
<div class="abs brand-box">
  <div class="brand-mark"></div>
  <div class="brand-name">Torvane<br>Health</div>
</div>
<nav class="nav">
  <a style="left:0">Home</a>
  <a style="left:71px">About Us</a>
  <a style="left:161px">Our Services</a>
  <a style="left:276px">Patient Information</a>
  <a style="left:433px">Our Resources</a>
  <a style="left:559px">Contact Us</a>
</nav>

<!-- hero -->
<div class="photo hero" role="img" aria-label="Smiling senior couple walking together on a leafy park path"></div>
<div class="abs hero-shade"></div>
<h1 class="abs heading hero-title">Torvane Health</h1>
<p class="abs hero-text">Lorem ipsum dolor sit amet, consectetur adipiscing elit, incididunt ut labore et dolore magna aliqua.</p>
<div class="btn" style="left:144px;top:440px;width:186px;height:45px;font-size:14px">Get Started <svg viewBox="0 0 12 12"><circle cx="6" cy="6" r="6" fill="#fff"/><path d="M5 3.5 7.5 6 5 8.5" stroke="#4a8a8a" stroke-width="1.6" fill="none"/></svg></div>
<div class="abs arrow-dark" style="left:46px;top:367px"><svg width="14" height="14" viewBox="0 0 14 14"><path d="M9 2 4 7l5 5" stroke="#fff" stroke-width="1.8" fill="none"/></svg></div>
<div class="abs arrow-dark" style="left:1115px;top:367px"><svg width="14" height="14" viewBox="0 0 14 14"><path d="m5 2 5 5-5 5" stroke="#fff" stroke-width="1.8" fill="none"/></svg></div>
<svg class="abs" style="left:0;top:585px" width="1200" height="155" viewBox="0 0 1200 155">
  <defs><linearGradient id="heroLine" x1="0" x2="1"><stop offset="0" stop-color="#3f77c2"/><stop offset="1" stop-color="#6aa740"/></linearGradient></defs>
  <path d="M0 40 Q520 200 1200 40 L1200 155 L0 155Z" fill="url(#heroLine)"/>
  <path d="M0 45 Q520 190 1200 70 L1200 155 L0 155Z" fill="#fff"/>
</svg>

<!-- about -->
<div class="abs about-panel" role="img" aria-label="Torvane Health brand panel"><span>Torvane Health</span></div>
<h2 class="abs heading section-title" style="left:664px;top:890px">About Us</h2>
<p class="abs body-copy" style="left:664px;top:957px;width:392px">Lorem ipsum dolor sit amet, consectetur adipiscing elit, sed do eiusmod tempor incididunt ut labore et dolore magna aliqua. Ut enim ad minim veniam, quis nostrud exercitation ullamco laboris nisi ut aliquip ex ea commodo consequat.</p>
<p class="abs body-copy" style="left:664px;top:1068px;width:392px">Duis aute irure dolor in reprehenderit in voluptate velit esse cillum dolore eu fugiat nulla pariatur. Excepteur sint occaecat cupidatat non proident, sunt in mollit anim id est laborum.</p>
<div class="btn" style="left:665px;top:1177px;width:165px;height:43px">Read More <svg viewBox="0 0 12 12"><circle cx="6" cy="6" r="6" fill="#fff"/><path d="M5 3.5 7.5 6 5 8.5" stroke="#4a8a8a" stroke-width="1.6" fill="none"/></svg></div>

<!-- services -->
<section class="abs services"></section>
<h2 class="abs heading section-title" style="left:0;width:1200px;top:1434px;text-align:center;font-size:31px">Our Services</h2>

<div class="card" style="left:144px;top:1516px;height:411px">
  <div class="photo" role="img" aria-label="Patient receiving hemodialysis in a clinic chair" style="background:linear-gradient(135deg,#c8d7ea,#5a79a8)"></div>
  <div class="icon"><svg width="30" height="30" viewBox="0 0 24 24" fill="none" stroke="#fff" stroke-width="1.5"><rect x="6" y="3" width="12" height="14" rx="1"/><path d="M9 7h6M9 10h6M12 17v4M8 21h8"/></svg></div>
  <h3>Hemodialysis</h3>
  <p>Sed ut perspiciatis unde omnis iste natus sit voluptatem accusantium doloremque laudantium, totam rem aperiam,</p>
  <div class="btn">Read More <svg viewBox="0 0 12 12"><circle cx="6" cy="6" r="6" fill="#fff"/><path d="M5 3.5 7.5 6 5 8.5" stroke="#4a8a8a" stroke-width="1.6" fill="none"/></svg></div>
</div>

<div class="card" style="left:457px;top:1533px;height:409px">
  <div class="photo" role="img" aria-label="Arm connected to peritoneal dialysis tubing" style="background:linear-gradient(135deg,#e4d9cf,#8f8a86)"></div>
  <div class="icon"><svg width="30" height="30" viewBox="0 0 24 24" fill="none" stroke="#fff" stroke-width="1.5"><rect x="4" y="4" width="16" height="16" rx="2"/><path d="M8 9h8M8 13h5M12 4v-2"/></svg></div>
  <h3>Peritoneal Dialysis</h3>
  <p>Sed ut perspiciatis unde omnis iste natus sit voluptatem accusantium doloremque laudantium, totam rem aperiam,</p>
  <div class="btn">Read More <svg viewBox="0 0 12 12"><circle cx="6" cy="6" r="6" fill="#fff"/><path d="M5 3.5 7.5 6 5 8.5" stroke="#4a8a8a" stroke-width="1.6" fill="none"/></svg></div>
</div>

<div class="card" style="left:767px;top:1516px;height:411px">
  <div class="photo" role="img" aria-label="Nurse preparing a patient's arm for home hemodialysis" style="background:linear-gradient(135deg,#b9cfd8,#566f5a)"></div>
  <div class="icon"><svg width="30" height="30" viewBox="0 0 24 24" fill="none" stroke="#fff" stroke-width="1.5"><path d="M3 11 12 4l9 7"/><path d="M6 10v10h12V10"/><path d="M12 12v5M9.5 14.5h5"/></svg></div>
  <h3>Home Hemodialysis</h3>
  <p>Sed ut perspiciatis unde omnis iste natus sit voluptatem accusantium doloremque laudantium, totam rem aperiam,</p>
  <div class="btn">Read More <svg viewBox="0 0 12 12"><circle cx="6" cy="6" r="6" fill="#fff"/><path d="M5 3.5 7.5 6 5 8.5" stroke="#4a8a8a" stroke-width="1.6" fill="none"/></svg></div>
</div>

<!-- holiday band -->
<section class="abs band">
  <h2 class="heading">Plan your holiday dialysis in our<br>network of centres</h2>
  <p>Sed ut perspiciatis unde omnis iste natus error sit voluptatem accusantium doloremque laudantium, totam rem aperi eaque ipsa quae ab illo inventore veritatis et quasi architecto beatae vitae dicta sunt explicabo.</p>
  <div class="call-pill"><span class="ico"><svg width="16" height="16" viewBox="0 0 24 24" fill="#fff"><path d="M6.6 10.8a15 15 0 0 0 6.6 6.6l2.2-2.2c.3-.3.7-.4 1-.2 1.1.4 2.3.6 3.6.6.6 0 1 .4 1 1V20c0 .6-.4 1-1 1A17 17 0 0 1 3 4c0-.6.4-1 1-1h3.5c.6 0 1 .4 1 1 0 1.3.2 2.5.6 3.6.1.3 0 .7-.2 1z"/></svg></span>Call us at 888-888-8888</div>
</section>

<!-- clinic -->
<h2 class="abs heading section-title" style="left:144px;top:2518px">Our Clinic</h2>
<p class="abs body-copy" style="left:144px;top:2587px;width:420px">Lorem ipsum dolor sit amet, consectetur adipiscing elit, sed do eiusmod tempor incididunt ut labore et dolore magna aliqua. Ut enim ad minim veniam, quis nostrud exercitation ullamco laboris nisi ut aliquip ex ea commodo consequat.</p>
<p class="abs body-copy" style="left:144px;top:2698px;width:420px">Sed ut perspiciatis unde omnis iste natus error sit voluptatem accusantium doloremque laudantium, totam rem aperiam, eaque ipsa quae ab illo inventore veritatis et quasi architecto beatae vitae dicta voluptatem quia voluptas sit  enim ipsam  sunt explicabo.</p>
<div class="btn" style="left:145px;top:2829px;width:187px;height:50px;font-size:14px">Read More <svg viewBox="0 0 12 12"><circle cx="6" cy="6" r="6" fill="#fff"/><path d="M5 3.5 7.5 6 5 8.5" stroke="#4a8a8a" stroke-width="1.6" fill="none"/></svg></div>
<svg class="abs" style="left:630px;top:2488px" width="440" height="440" viewBox="0 0 440 440">
  <path d="M372 92 A200 200 0 1 0 60 340" fill="none" stroke="#3f77c2" stroke-width="14"/>
  <path d="M378 104 A205 205 0 0 1 120 398" fill="none" stroke="#6aa740" stroke-width="18"/>
</svg>
<div class="photo" role="img" aria-label="Bright dialysis treatment room with reclining chairs and machines" style="left:656px;top:2527px;width:380px;height:380px;border-radius:50%;background:radial-gradient(circle at 45% 40%,#f1f3f5,#b5bcc4 70%,#8d96a0)"></div>
<div class="photo" role="img" aria-label="Clinician operating a dialysis machine" style="left:634px;top:2752px;width:206px;height:206px;border-radius:50%;border:5px solid #fff;background:linear-gradient(150deg,#e4c770,#7fa0bf 60%,#48698c)"></div>

<!-- testimonials -->
<svg class="abs" style="left:0;top:3030px" width="1200" height="560" viewBox="0 0 1200 560">
  <defs><linearGradient id="tBand" x1="0" x2="1"><stop offset="0" stop-color="#3f77c2"/><stop offset="1" stop-color="#6aa740"/></linearGradient></defs>
  <path d="M0 115 Q600 -115 1200 115 L1200 475 Q600 639 0 475Z" fill="url(#tBand)"/>
</svg>
<h2 class="abs heading t-title">Clients Testimonial</h2>
<svg class="abs" style="left:78px;top:3328px" width="22" height="30" viewBox="0 0 22 30"><path d="M16 3 5 15l11 12" stroke="#fff" stroke-width="3.5" fill="none"/></svg>
<svg class="abs" style="left:1099px;top:3328px" width="22" height="30" viewBox="0 0 22 30"><path d="m6 3 11 12L6 27" stroke="#fff" stroke-width="3.5" fill="none"/></svg>

<div class="t-card" style="left:205px">
  <div class="quote">&ldquo;</div>
  <p>Sed ut perspiciatis unde omnis iste natus sit voluptatem accusantium doloremque laudantium, totam rem aperiam,</p>
  <h4>John Doe</h4>
  <div class="stars">★★★★★</div>
</div>
<div class="avatar" role="img" aria-label="Client portrait" style="left:158px;top:3288px"></div>

<div class="t-card" style="left:662px">
  <div class="quote">&ldquo;</div>
  <p>Sed ut perspiciatis unde omnis iste natus sit voluptatem accusantium doloremque laudantium, totam rem aperiam,</p>
  <h4>John Doe</h4>
  <div class="stars">★★★★★</div>
</div>
<div class="avatar" role="img" aria-label="Client portrait" style="left:613px;top:3288px"></div>

<!-- blog -->
<h2 class="abs heading section-title" style="left:0;width:1200px;top:3657px;text-align:center;font-size:35px">Our Blog</h2>
<div class="abs blog-grid"></div>

<div class="blog-cell" style="left:146px;top:3750px">
  <div class="date"><svg width="11" height="11" viewBox="0 0 12 12" fill="none" stroke="#6aa740" stroke-width="1.4"><circle cx="6" cy="6" r="5"/><path d="M6 3v3l2 1"/></svg>18 Dec, 2023</div>
  <h3>Sed ut perspiciatis unde omnis iste natus error</h3>
  <p>Lorem ipsum dolor sit amet, consectetur ncididunt ut labore et dolore magna aliqua. Ut enim ad minim veniam,</p>
  <div class="btn">Read More <svg viewBox="0 0 12 12"><circle cx="6" cy="6" r="6" fill="#fff"/><path d="M5 3.5 7.5 6 5 8.5" stroke="#3f77c2" stroke-width="1.6" fill="none"/></svg></div>
</div>
<div class="photo" role="img" aria-label="Close-up of dialysis tubing and blood lines" style="left:449px;top:3750px;width:303px;height:269px;background:linear-gradient(140deg,#d9cfcf,#9c5b5f 55%,#7d8a96)"></div>
<div class="blog-cell" style="left:752px;top:3750px">
  <div class="date"><svg width="11" height="11" viewBox="0 0 12 12" fill="none" stroke="#6aa740" stroke-width="1.4"><circle cx="6" cy="6" r="5"/><path d="M6 3v3l2 1"/></svg>18 Dec, 2023</div>
  <h3>Sed ut perspiciatis unde omnis iste natus error</h3>
  <p>Lorem ipsum dolor sit amet, consectetur ncididunt ut labore et dolore magna aliqua. Ut enim ad minim veniam,</p>
  <div class="btn">Read More <svg viewBox="0 0 12 12"><circle cx="6" cy="6" r="6" fill="#fff"/><path d="M5 3.5 7.5 6 5 8.5" stroke="#3f77c2" stroke-width="1.6" fill="none"/></svg></div>
</div>

<div class="photo" role="img" aria-label="Doctor and nurse attending a patient in a dialysis chair" style="left:146px;top:4019px;width:303px;height:269px;background:linear-gradient(140deg,#e2dcd2,#a9a6a6 55%,#6f7c8c)"></div>
<div class="blog-cell" style="left:449px;top:4019px">
  <svg class="abs" style="left:140px;top:-10px" width="22" height="11" viewBox="0 0 22 11"><path d="M0 11 11 0l11 11Z" fill="#fff"/></svg>
  <div class="date"><svg width="11" height="11" viewBox="0 0 12 12" fill="none" stroke="#6aa740" stroke-width="1.4"><circle cx="6" cy="6" r="5"/><path d="M6 3v3l2 1"/></svg>18 Dec, 2023</div>
  <h3>Sed ut perspiciatis unde omnis iste natus error</h3>
  <p>Lorem ipsum dolor sit amet, consectetur ncididunt ut labore et dolore magna aliqua. Ut enim ad minim veniam,</p>
  <div class="btn">Read More <svg viewBox="0 0 12 12"><circle cx="6" cy="6" r="6" fill="#fff"/><path d="M5 3.5 7.5 6 5 8.5" stroke="#3f77c2" stroke-width="1.6" fill="none"/></svg></div>
</div>
<div class="photo" role="img" aria-label="Empty clinic treatment room with dialysis equipment" style="left:752px;top:4019px;width:302px;height:269px;background:linear-gradient(140deg,#eef0f0,#b9c0c4 55%,#8a9299)"></div>

<!-- footer -->
<svg class="abs" style="left:0;top:4380px" width="1200" height="386" viewBox="0 0 1200 386">
  <path d="M0 90 Q600 -90 1200 90 L1200 386 L0 386Z" fill="#050505"/>
</svg>
<div class="abs" style="left:144px;top:4530px;width:190px;display:flex;flex-direction:column;align-items:center;gap:12px">
  <div class="brand-mark" style="width:40px;height:40px"></div>
  <div class="brand-name" style="font-size:26px;line-height:28px">Torvane<br>Health</div>
</div>

<div class="foot-title" style="left:409px">Our Office Address</div>
<div class="foot-item" style="top:4530px"><svg width="12" height="12" viewBox="0 0 24 24" fill="#6aa740"><path d="M6.6 10.8a15 15 0 0 0 6.6 6.6l2.2-2.2c.3-.3.7-.4 1-.2 1.1.4 2.3.6 3.6.6.6 0 1 .4 1 1V20c0 .6-.4 1-1 1A17 17 0 0 1 3 4c0-.6.4-1 1-1h3.5c.6 0 1 .4 1 1 0 1.3.2 2.5.6 3.6.1.3 0 .7-.2 1z"/></svg><div><b>Phone</b>0800 314 272</div></div>
<div class="foot-item" style="top:4578px"><svg width="12" height="12" viewBox="0 0 24 24" fill="#6aa740"><path d="M2 5h20v14H2z"/><path d="m2 5 10 8 10-8" stroke="#050505" stroke-width="2" fill="none"/></svg><div><b>Email</b>info@torvanehealth.com</div></div>
<div class="foot-item" style="top:4626px"><svg width="12" height="14" viewBox="0 0 24 28" fill="#6aa740"><path d="M12 0a9 9 0 0 0-9 9c0 7 9 19 9 19s9-12 9-19a9 9 0 0 0-9-9zm0 12a3 3 0 1 1 0-6 3 3 0 0 1 0 6z"/></svg><div style="width:185px"><b>Location</b>Lorem ipsum dolor consectetur adipiscing elit, sed do</div></div>

<div class="foot-title" style="left:690px">Company</div>
<ul class="foot-links">
  <li>Home</li><li>About Us</li><li>Our Services</li><li>Patient Information</li><li>Resources</li><li>Contact Us</li>
</ul>

<div class="foot-title" style="left:843px">Still Have Questions?</div>
<p class="foot-note">Contact us using this form. A representative will answer your questions as soon as possible.</p>
<div class="btn" style="left:843px;top:4650px;width:187px;height:40px;font-size:13px;background:linear-gradient(90deg,#3f77c2,#4b8ab0)">Get a Quote</div>

<div class="abs" style="left:144px;top:4700px;width:910px;height:1px;background:#6b6b6b"></div>
<div class="abs" style="left:980px;top:4690px;width:76px;height:18px;border-radius:9px;background:#8a8a8a;color:#fff;font-size:9.5px;font-weight:700;display:flex;align-items:center;justify-content:center;gap:4px">
  <svg width="8" height="8" viewBox="0 0 8 8"><path d="M4 0 0 4h2.5v4h3V4H8Z" fill="#fff"/></svg>Go Up
</div>
<div class="foot-bottom" style="left:146px">© 2024 Torvane Health | All Rights Reserved</div>
<span class="social" style="left:563px"></span>
<span class="social" style="left:592px"></span>
<span class="social" style="left:621px"></span>
<div class="foot-bottom" style="left:749px">Privacy Policy &nbsp;|&nbsp; Cookie Policy &nbsp;|&nbsp; Terms Of Services</div>

</body>
</html>
```